Banner Design Project

We are an Australian online lighting store based in Sydney.
Our website is "www.trelvamart.com.au"
We need someone you can create a 2 banners for our homepage.
We will have 3 banners rotating, the first banner will be our actual banner, the second one will be advertising Free Shipping Insurance and the third will advertising the 30 Day money back guaranty.
Don't be afraid to use words like Risk Free, 30 Day Money back Guaranty! etc....
The banner size:
599 x 186 px
The format should be given in .psd and .jpg
We need something slick and attractive that looks very promotional.
The banner should have the same look and feel as the website.
We are looking for someone long term, so if the job goes well, we might ask the person to design regularly for us in the future.

```html
<!DOCTYPE html>
<html lang="en">
<head>
<meta charset="utf-8">
<title>Trelvamart – 30 Day Money Back Guarranty</title>
<link rel="stylesheet" href="https://fonts.googleapis.com/css2?family=Arvo:wght@700&display=swap">
<style>
  :root {
    --sky-top: #ffffff;
    --sky-bottom: #d6ecf7;
    --orange-light: #fbb04a;
    --orange-mid: #f58a1f;
    --orange-dark: #e26d0c;
    --orange-fold: #a9500a;
    --sash-blue: #1f6a9c;
    --sash-blue-dark: #15527b;
    --brand-grey: #6d6d6d;
    --white: #ffffff;
    --photo-light: #d9cbb8;
    --photo-dark: #9c8466;
  }
  html, body {
    margin: 0;
    padding: 0;
    overflow: hidden;
    background: #ffffff;
  }
  .banner {
    position: relative;
    width: 1200px;
    height: 373px;
    overflow: hidden;
    background: radial-gradient(ellipse at 45% 30%, var(--sky-top) 0%, var(--sky-top) 35%, var(--sky-bottom) 100%);
    font-family: "Arvo", "Rockwell", serif;
  }
  .ribbon {
    position: absolute;
    left: 0;
    top: 0;
  }
  .ribbon-text {
    position: absolute;
    left: 180px;
    top: 70px;
    width: 720px;
    margin: 0;
    text-align: center;
    color: var(--white);
    font-size: 60px;
    line-height: 68px;
    font-weight: 700;
    text-shadow: 0 2px 3px rgba(150, 70, 0, 0.45);
  }
  .brand-name {
    position: absolute;
    left: 350px;
    top: 262px;
    width: 420px;
    margin: 0;
    text-align: center;
    color: var(--brand-grey);
    font-size: 64px;
    line-height: 80px;
    font-weight: 700;
    letter-spacing: -1px;
  }
  .product-photo {
    position: absolute;
    left: 900px;
    top: 60px;
    width: 290px;
    height: 290px;
    background: linear-gradient(180deg, var(--photo-light) 0%, var(--photo-dark) 100%);
  }
  .sash {
    position: absolute;
    right: -70px;
    top: 28px;
    width: 320px;
    height: 84px;
    transform: rotate(45deg);
    background: linear-gradient(180deg, var(--sash-blue) 0%, var(--sash-blue-dark) 100%);
    color: var(--white);
    text-align: center;
    font-size: 34px;
    line-height: 40px;
    font-weight: 700;
    font-style: italic;
    padding-top: 2px;
    box-shadow: 0 3px 6px rgba(0, 0, 0, 0.3);
  }
</style>
</head>
<body>
  <div class="banner">
    <svg class="ribbon" width="940" height="260" viewBox="0 0 940 260" aria-hidden="true">
      <defs>
        <linearGradient id="ribbonFace" x1="0" y1="0" x2="0" y2="1">
          <stop offset="0" stop-color="var(--orange-light)"/>
          <stop offset="0.55" stop-color="var(--orange-mid)"/>
          <stop offset="1" stop-color="var(--orange-dark)"/>
        </linearGradient>
        <linearGradient id="ribbonTail" x1="0" y1="0" x2="0" y2="1">
          <stop offset="0" stop-color="#f49a35"/>
          <stop offset="1" stop-color="#d8680c"/>
        </linearGradient>
      </defs>
      <polygon class="ribbon-tail" points="30,100 220,100 220,250 30,250 75,175" fill="url(#ribbonTail)"/>
      <polygon class="ribbon-fold" points="180,216 220,216 220,250" fill="var(--orange-fold)"/>
      <path class="ribbon-face" d="M180,46 Q540,32 910,46 L910,216 Q540,202 180,216 Z" fill="url(#ribbonFace)"/>
    </svg>

    <h1 class="ribbon-text">30 Day Money<br>Back Guarranty</h1>

    <p class="brand-name">trelvamart</p>

    <div class="product-photo" role="img" aria-label="Product photo: bronze pendant lamp with a bare bulb hanging from a cord"></div>

    <div class="sash">Risk<br>Free!</div>
  </div>
</body>
</html>
```